I’d like to see something with similar colors and design concept to the “Your Fortune Starts at Breakfast” book included in attchment

Create a book cover with front cover, and full front, spine and back cover spread.
Simple and clean design. See design inspiration below.
Size 6X9
Title of the book: Write Onward! Veteran Editors Reveal Their Methods

Please leave space for 6 authors names on the front cover. Authors names will be provided at a later time.

Back of book should included the name of the publishing company:
Bright Lantern Publishing

As well as the following synopsis
The landscape of the publishing industry is changing. Gone are the days of coveted gatekeepers controlling content and dictating the messages being distributed. With the rise of technology, social media , self-publishing platforms, and independent bookstores, there are increased opportunities for people to share their ideas, messages, and stories with the world through books. The types of books that we’re publishing are also evolving — mini-books, audio books, journals, multi-author books, cook books, children’s books, comic books, coloring books, interactive books, tarot and oracle card decks are all expanding the podium for people to express ideas and influence the culture. More and more entrepreneurs are posturing themselves as thought leaders by leveraging this growing platform.
But that doesn't mean it’s easy.
Even with the expanding platforms and opportunities, only a fraction of people with publishing ambitions are able to achieve this coveted dream held by so many. It can be a daunting process for budding authors trying to maneuver through the writing, packaging, marketing, and publishing processes alone.

In this book you'll find passionate, purpose-driven, and well-versed experts working in the various areas of publishing, eager to help open your eyes to the promise of publishing and effortlessly guide you through the process.

Colors
0094D4
00A9DD
6FCCEA
C7EBF8
E9F6FB
FFF300
FFF600
FEFA6F
FFFEC7
FFFEE8
FFC000
F8CF3A
FAE287
FDF2CF
FEFAEE
F0912C
F2A743
F7CA91
FBE8D2
FDF5EE
EE7325
F08F49
F5BC92
FAE3D3
FDF4ED
6B429C
8869AF
B7A5CE
E3DAEB
F3F0F8

```html
<!DOCTYPE html>
<html lang="en">
<head>
<meta charset="utf-8">
<title>Write Onward! – Cover Spread</title>
<link rel="stylesheet" href="https://fonts.googleapis.com/css2?family=Comfortaa:wght@300;400;700&family=Questrial&display=swap">
<style>
  :root {
    --paper: #ffffff;
    --cover-yellow: #f2d019;
    --accent-red: #e8453c;
    --accent-teal: #4e9aa6;
    --steel-light: #b4bcbc;
    --steel-dark: #5c5836;
  }
  html, body {
    margin: 0;
    padding: 0;
    width: 1200px;
    height: 864px;
    overflow: hidden;
    background: var(--paper);
  }
  .spread {
    position: relative;
    width: 1200px;
    height: 864px;
  }
  .panel {
    position: absolute;
    background: var(--cover-yellow);
  }
  .back-cover  { left: 25px;  top: 24px; width: 531px; height: 816px; }
  .spine       { left: 576px; top: 23px; width: 48px;  height: 816px; }
  .front-cover { left: 646px; top: 23px; width: 531px; height: 816px; }

  .synopsis {
    position: absolute;
    left: 29px;
    top: 26px;
    width: 473px;
    font-family: "Comfortaa", sans-serif;
    font-weight: 400;
    font-size: 17.6px;
    line-height: 20.3px;
    color: var(--accent-red);
    text-align: justify;
  }
  .synopsis p {
    margin: 0 0 7px;
    text-indent: 17px;
  }
  .publisher {
    position: absolute;
    right: 22px;
    top: 738px;
    margin: 0;
    font-family: "Comfortaa", sans-serif;
    font-weight: 400;
    font-size: 25px;
    line-height: 30px;
    color: var(--accent-teal);
    text-align: right;
  }
  .spine svg, .front-cover svg {
    position: absolute;
    left: 0;
    top: 0;
  }
  .spine-title {
    font-family: "Comfortaa", sans-serif;
    font-weight: 400;
    font-size: 34px;
    fill: var(--accent-red);
  }
  .title-main {
    font-family: "Comfortaa", sans-serif;
    font-weight: 700;
    font-size: 104px;
  }
  .title-sub {
    font-family: "Comfortaa", sans-serif;
    font-weight: 400;
    font-size: 74px;
  }
  .title-sub.teal { fill: var(--accent-teal); }
  .title-sub.red  { fill: var(--accent-red); }
  .author-name {
    font-family: "Questrial", sans-serif;
    font-size: 28px;
    letter-spacing: 0.5px;
  }
</style>
</head>
<body>
<main class="spread">

  <section class="panel back-cover">
    <div class="synopsis">
      <p>The landscape of the publishing industry is changing. Gone are the days of coveted gatekeepers controlling content and dictating the messages being distributed. With the rise of technology, social media , self-publishing platforms, and independent bookstores, there are increased opportunities for people to share their ideas, messages, and stories with the world through books. The types of books that we’re publishing are also evolving – mini-books, audio books, journals, multi-author books, cook books, children’s books, comic books, coloring books, interactive books, tarot and oracle card decks are all expanding the podium for people to express ideas and influence the culture. More and more entrepreneurs are posturing themselves as thought leaders by leveraging this growing platform.</p>
      <p>But that doesn't mean it’s easy.</p>
      <p>Even with the expanding platforms and opportunities, only a fraction of people with publishing ambitions are able to achieve this coveted dream held by so many. It can be a daunting process for budding authors trying to maneuver through the writing, packaging, marketing, and publishing processes alone.</p>
    </div>
    <p class="publisher">Bright Lantern<br>Publishing</p>
  </section>

  <section class="panel spine">
    <svg width="48" height="816" viewBox="0 0 48 816">
      <text class="spine-title" transform="translate(36 792) rotate(-90)" textLength="762" lengthAdjust="spacingAndGlyphs">Write Onward! Veteran Editors Reveal Their Methods</text>
    </svg>
  </section>

  <section class="panel front-cover">
    <svg width="531" height="816" viewBox="0 0 531 816">
      <defs>
        <linearGradient id="steel-fill-main" x1="0" y1="0" x2="0" y2="1">
          <stop offset="0" stop-color="var(--steel-light)"/>
          <stop offset="0.5" stop-color="var(--steel-dark)"/>
          <stop offset="1" stop-color="var(--steel-light)"/>
        </linearGradient>
        <linearGradient id="steel-fill-names" x1="0" y1="0" x2="0" y2="1">
          <stop offset="0" stop-color="#5c5836"/>
          <stop offset="1" stop-color="#a3a8a4"/>
        </linearGradient>
      </defs>

      <g class="book-title">
        <text class="title-main" x="12" y="102" fill="url(#steel-fill-main)" textLength="300" lengthAdjust="spacingAndGlyphs">WRITE</text>
        <text class="title-main" x="12" y="196" fill="url(#steel-fill-main)" textLength="490" lengthAdjust="spacingAndGlyphs">ONWARD!</text>
        <text class="title-sub teal" x="17" y="273" textLength="310" lengthAdjust="spacingAndGlyphs">VETERAN</text>
        <text class="title-sub red"  x="17" y="347" textLength="280" lengthAdjust="spacingAndGlyphs">EDITORS</text>
        <text class="title-sub teal" x="15" y="421" textLength="235" lengthAdjust="spacingAndGlyphs">REVEAL</text>
        <text class="title-sub red"  x="15" y="494" textLength="470" lengthAdjust="spacingAndGlyphs">THEIR METHODS</text>
      </g>

      <g class="author-list" text-anchor="end" fill="url(#steel-fill-names)">
        <text class="author-name" x="503" y="579">&gt;&gt;&gt; AUTOR 001 PETROVAN &gt;&gt;&gt;</text>
        <text class="author-name" x="503" y="620">&gt;&gt;&gt; AUTOR 002 DRAGANIC &gt;&gt;&gt;</text>
        <text class="author-name" x="503" y="660">&gt;&gt;&gt; AUTOR 003 VELIKIC &gt;&gt;&gt;</text>
        <text class="author-name" x="503" y="701">&gt;&gt;&gt; JONAS 004 REED &gt;&gt;&gt;</text>
        <text class="author-name" x="503" y="741">&gt;&gt;&gt; OSCAR 007 LANE &gt;&gt;&gt;</text>
        <text class="author-name" x="503" y="782">&gt;&gt;&gt; HELLO 006 WORLD</text>
      </g>
    </svg>
  </section>

</main>
</body>
</html>
```